TG - management consultant

Business card - contemporary design

Front info
Thomas Galloway

(Address not necessary)
PO Box 7324
Ashby, CA 94071

(650) 482-3719
tg@thomasgallo.wy

Twitter: tgq287
Facebook: /Thomas.Galloway
Linkedin: /in/thomasgalloway

Back or Front
www.thomasgalloway.net
Facilitation & coaching, change management, strategic partnerships, business improvement

Target Market(s)

High tech businesses - mostly startups in Silicon Valley

Industry/Entity Type

Business

Font styles to use
Sans Serif

Colors

Designer to choose colors to be used in the design.

```html
<!DOCTYPE html>
<html lang="en">
<head>
<meta charset="utf-8">
<title>Thomas Galloway – Business Card</title>
<link rel="stylesheet" href="https://fonts.googleapis.com/css2?family=Lato:wght@400;700;900&family=Open+Sans:wght@400;700&family=PT+Serif&display=swap">
<style>
  :root {
    --stage: #e9eaec;
    --card-white: #ffffff;
    --panel-dark: #2f2f30;
    --accent: #3fc0ea;
    --accent-soft: #5ccaee;
    --accent-pale: #cfe8f3;
    --ink: #222222;
    --ink-grey: #6d6e70;
    --icon-grey: #c9c9c9;
    --text-light: #e4e4e4;
  }
  * { box-sizing: border-box; margin: 0; padding: 0; }
  html, body { width: 1200px; height: 900px; overflow: hidden; }
  body {
    background: var(--stage);
    font-family: "Lato", sans-serif;
    position: relative;
  }
  .card {
    position: absolute;
    left: 260px;
    width: 680px;
    height: 388px;
    background: var(--card-white);
    box-shadow: 0 6px 18px rgba(0,0,0,.15);
    overflow: hidden;
  }
  .card--back { top: 50px; }
  .card--front { top: 462px; display: flex; }

  /* Back */
  .back__url {
    position: absolute;
    top: 34px;
    right: 40px;
    font-family: "Open Sans", sans-serif;
    font-weight: 700;
    font-size: 34px;
    color: var(--ink);
    letter-spacing: .2px;
  }
  .back__url .tld { font-weight: 400; color: #444; }
  .back__bubble {
    position: absolute;
    left: 40px;
    top: 104px;
    width: 600px;
    height: 250px;
  }
  .back__services {
    position: absolute;
    left: 82px;
    top: 140px;
    width: 520px;
    font-family: "PT Serif", serif;
    font-size: 31px;
    line-height: 1.25;
    color: #ffffff;
  }

  /* Front */
  .front__identity {
    width: 55%;
    position: relative;
    background: var(--card-white);
  }
  .front__name {
    position: absolute;
    left: 34px;
    bottom: 46px;
    font-size: 48px;
    line-height: 1;
    letter-spacing: 1px;
  }
  .front__first { display: block; color: var(--ink-grey); font-weight: 400; }
  .front__last { display: block; color: var(--accent); font-weight: 900; margin-top: 4px; }

  .front__panel {
    width: 45%;
    background: var(--panel-dark);
    padding: 40px 12px 0 26px;
    color: var(--accent);
  }
  .contact { list-style: none; }
  .contact li {
    display: flex;
    align-items: center;
    gap: 11px;
    font-size: 15.5px;
    line-height: 1.2;
    margin-bottom: 10px;
    white-space: nowrap;
  }
  .contact svg { flex: 0 0 16px; }
  .social { list-style: none; margin-top: 34px; }
  .social li {
    display: flex;
    align-items: center;
    gap: 14px;
    margin-bottom: 14px;
    color: var(--text-light);
    font-size: 17px;
    line-height: 1.1;
  }
  .social__dot {
    flex: 0 0 38px;
    height: 38px;
    border-radius: 50%;
    background: var(--accent);
  }
</style>
</head>
<body>

<section class="card card--back" aria-label="Business card back">
  <div class="back__url">www.thomasgalloway<span class="tld">.net</span></div>
  <svg class="back__bubble" viewBox="0 0 600 250" aria-hidden="true">
    <polygon points="0,200 600,120 600,250 0,250" fill="var(--accent-pale)" opacity=".7"/>
    <rect x="10" y="0" width="580" height="190" rx="10" fill="var(--accent-soft)"/>
    <polygon points="60,185 110,185 78,225" fill="var(--accent-soft)"/>
  </svg>
  <p class="back__services">Facilitation &amp; coaching, change Management, strategic partnerships, Business improvement</p>
</section>

<section class="card card--front" aria-label="Business card front">
  <div class="front__identity">
    <h1 class="front__name">
      <span class="front__first">THOMAS</span>
      <span class="front__last">GALLOWAY</span>
    </h1>
  </div>
  <div class="front__panel">
    <ul class="contact">
      <li>
        <svg width="16" height="18" viewBox="0 0 16 18" aria-hidden="true"><path d="M8 0a6 6 0 0 0-6 6c0 4.5 6 12 6 12s6-7.5 6-12a6 6 0 0 0-6-6zm0 8.5A2.5 2.5 0 1 1 8 3.5a2.5 2.5 0 0 1 0 5z" fill="var(--icon-grey)"/></svg>
        PO Box 7324, Ashby, CA 94071
      </li>
      <li>
        <svg width="16" height="18" viewBox="0 0 16 18" aria-hidden="true"><rect x="4" y="0" width="9" height="18" rx="2" fill="var(--icon-grey)"/><rect x="5.5" y="2.5" width="6" height="8" fill="var(--panel-dark)"/></svg>
        (650) 482-3719
      </li>
      <li>
        <svg width="16" height="12" viewBox="0 0 16 12" aria-hidden="true"><rect width="16" height="12" fill="var(--icon-grey)"/><path d="M0 0l8 6 8-6" fill="none" stroke="var(--panel-dark)" stroke-width="1.3"/></svg>
        tg@thomasgallo.wy
      </li>
    </ul>
    <ul class="social">
      <li><span class="social__dot" aria-hidden="true"></span><span>friendlink.com/<br>Thomas.Galloway</span></li>
      <li><span class="social__dot" aria-hidden="true"></span><span>workgrid.com/<br>in/thomasgalloway</span></li>
      <li><span class="social__dot" aria-hidden="true"></span><span>chirpline.com/<br>tgq287</span></li>
    </ul>
  </div>
</section>

</body>
</html>
```